Business Card + Stationery Design for a Craft Beer Bar

Mr. Tolvek's is a taproom sport bar that contains in its menu beers from different places around the world. What we offer differently is the experience that you can get inside our location, ambient music with rock from the 80s to 90s, projection with the sports of the moment, board games and private events.

Target Market(s)

Young people, Mid and High Class

Industry/Entity Type

Business

Font styles to use
Serif
Sans Serif

Colors
fee18a

Requirements
Must have
• Name, Title, Contact Details, Website
Nice to have
• Mail Signature
Should not have
• n/a

```html
<!DOCTYPE html>
<html lang="en">
<head>
<meta charset="utf-8">
<title>Mr. Tolvek's – Business Cards</title>
<link rel="stylesheet" href="https://fonts.googleapis.com/css2?family=Bebas+Neue&family=Mulish:wght@400;600;700&display=swap">
<style>
  :root {
    --stage: #dcdde0;
    --amber: #f0b858;
    --ink: #231f20;
    --paper: #ffffff;
    --rule: #7a7778;
    --ghost: #343132;
  }
  * { box-sizing: border-box; margin: 0; padding: 0; }
  html, body { width: 876px; height: 1200px; overflow: hidden; }
  body { background: var(--stage); position: relative; font-family: "Mulish", sans-serif; }

  .card { position: absolute; overflow: hidden; }
  .card--tall { top: 68px; width: 234px; height: 382px; }
  .card--square { width: 274px; height: 274px; border-radius: 16px; }
  .card--amber { background: var(--amber); color: var(--ink); }
  .card--ink { background: var(--ink); color: var(--paper); }
  .card--paper { background: var(--paper); color: var(--ink); box-shadow: 0 1px 3px rgba(0,0,0,.08); }

  .line { position: absolute; left: 0; right: 0; text-align: center; transform: translateY(-50%); white-space: nowrap; }
  .line--right { text-align: right; right: 14px; left: auto; }

  .wordmark { position: absolute; left: 0; right: 0; transform: translateY(-50%);
    display: flex; align-items: center; justify-content: center; gap: 8px; }
  .wordmark__dot { width: 14px; height: 14px; border-radius: 50%; flex: none; background: currentColor; }
  .wordmark__name { font-family: "Mulish", sans-serif; font-weight: 700; font-size: 24px; line-height: 1; white-space: nowrap; }
  .card--ink .wordmark { color: var(--paper); }

  .person { font-family: "Bebas Neue", sans-serif; color: var(--amber); line-height: 1; }
  .role { font-size: 10px; letter-spacing: .4px; }
  .role--condensed { font-family: "Bebas Neue", sans-serif; font-size: 12px; }
  .contact { font-size: 10.5px; font-weight: 600; }
  .web { font-size: 12.5px; font-weight: 600; letter-spacing: .3px; }
  .web b { color: var(--amber); font-weight: 700; }

  .rule { position: absolute; height: 1px; background: var(--rule); }
  .ghost-dot { position: absolute; left: -50px; top: 100px; width: 230px; height: 230px; border-radius: 50%; background: var(--ghost); }

  .signature-name { font-weight: 600; font-size: 12.5px; letter-spacing: .3px; }
</style>
</head>
<body>

  <!-- Vertical front, amber -->
  <section class="card card--tall card--amber" style="left:68px">
    <div class="wordmark" style="top:200px"><span class="wordmark__dot"></span><span class="wordmark__name">Mr. Tolvek's</span></div>
  </section>

  <!-- Vertical front, dark -->
  <section class="card card--tall card--ink" style="left:322px">
    <div class="wordmark" style="top:202px"><span class="wordmark__dot" style="background:var(--amber)"></span><span class="wordmark__name">Mr. Tolvek's</span></div>
  </section>

  <!-- Vertical back, contact -->
  <section class="card card--tall card--ink" style="left:575px">
    <span class="ghost-dot" aria-hidden="true"></span>
    <p class="line line--right person" style="top:38px;font-size:26px">YOUR NAME</p>
    <p class="line line--right role" style="top:60px">TITLE</p>
    <p class="line line--right contact" style="top:82px">info@MrTolveks.com</p>
    <p class="line line--right contact" style="top:100px">555.014.2287</p>
    <p class="line line--right web" style="top:362px">www.<b>MrTolveks</b>.com</p>
  </section>

  <!-- Square front, amber -->
  <section class="card card--square card--amber" style="left:154px;top:517px">
    <div class="wordmark" style="top:150px"><span class="wordmark__dot"></span><span class="wordmark__name">Mr. Tolvek's</span></div>
  </section>

  <!-- Square back, contact -->
  <section class="card card--square card--ink" style="left:448px;top:517px">
    <p class="line person" style="top:102px;font-size:20px">YOUR NAME</p>
    <p class="line role role--condensed" style="top:118px">TITLE</p>
    <span class="rule" style="left:0;width:208px;top:138px"></span>
    <p class="line contact" style="top:151px">info@MrTolveks.com</p>
    <p class="line contact" style="top:165px">555.014.2287</p>
    <span class="rule" style="left:66px;right:0;top:179px"></span>
    <p class="line web" style="top:248px">www.<b>MrTolveks</b>.com</p>
  </section>

  <!-- Square dark, name with website -->
  <section class="card card--square card--ink" style="left:154px;top:858px">
    <div class="wordmark" style="top:120px"><span class="wordmark__dot" style="background:var(--amber)"></span><span class="wordmark__name">Mr. Tolvek's</span></div>
    <p class="line web" style="top:248px">www.<b>MrTolveks</b>.com</p>
  </section>

  <!-- Square white, all-in-one -->
  <section class="card card--square card--paper" style="left:448px;top:858px">
    <div class="wordmark" style="top:120px"><span class="wordmark__dot"></span><span class="wordmark__name">Mr. Tolvek's</span></div>
    <p class="line signature-name" style="top:221px">YOUR NAME</p>
    <p class="line role" style="top:233px">TITLE</p>
    <p class="line contact" style="top:248px;font-weight:400">555.014.2287 / info@MrTolveks.com</p>
  </section>

</body>
</html>
```